依頼詳細
今回は、トップページデザインの募集になります。
レスポンシブデザインのサイトで、bootstrap4を利用しコーディングする予定になります。
デザイン幅は2000px、コンテンツの幅はbootstrap4デフォルトの1110pxを基準としてください。ただし最近のデザインの流行を取りいれて、フルワイドや、1200~15000px程度の幅のコンテンツをバランスよくレイアウトしてください。
コンテンツ配置は基本12分割になります。がデザインによっては、多少逸脱してもかまいません。
念のため、サンプルのPSDデータを添付しますので、参照ください。

本文のフォントはゴシック系は游ゴシック、メイリオ、明朝系は遊明朝でお願いします。
飾り文字はフリーフォントか、googleフォントを利用してください。

メイン画像部分・グローバルメニューは、ワイド適用でお願いします。

資料上はサイト名(社名)や住所などは伏字にしております。ご提案時点ではそのまま作成をお願いします。当選確定後、本内容に修正をお願いいたします。

当選の方は、希望があれば引き続き下層ページの作成及びコーディング作業を依頼可能です。
不明点、質問などありましたらメッセージ等でご連絡ください。

・カラー
青系(爽やかなイメージ)

・掲載画像
必ず添付ファイルを使用してください。
また、雰囲気が合っていれば、指定外の画像を背景などに使用いただいてもOKです。

・その他
内容詳細に関しては、別添のExcel資料を参照してください。
ページ数
1ページ
希望イメージ
シンプル 複雑
単色 カラフル
暗い 明るい
日常 高級
遊び心 厳粛
未来的 伝統的
女性的 男性的
希望する色
青系、水色系
納品ファイル
• 高解像度JPG (.jpg)
• フォトショップ形式 (.psd)
補足説明
納品ファイルは、PDF及びクライアント表示確認用のJPGを準備お願いします。
■ 選んだ理由

今回は、贅沢さや豪華さをイメージさせる洗練された先進的なデザインを希望しており、見た目が大事な案件でした。
業界的に国内外問わず「サイトの見た目」をかなり重要視しているため、"見栄えのするデザイン"というところに重きを置いてクライアントとの折衝の結果、skytrailふじさわ様を選定させていただきました。

■ 提案者全員のお礼・コメント

どの案も制作意図を組んでいただきとてもよかったのですが、今回はskytrailふじさわ様を当選とさせていただきました。
皆様ご提案ありがとうございました。
今後ともご提案宜しくお願いいたします。

```html
<!DOCTYPE html>
<html lang="ja">
<head>
<meta charset="UTF-8">
<title>SAFETY HIGH QUALITY</title>
<link href="https://fonts.googleapis.com/css2?family=Montserrat:wght@400;500;600;700&family=Noto+Sans+JP:wght@400;500;700&display=swap" rel="stylesheet">
<style>
:root{
  --blue:#1e64b4;
  --blue-dark:#154f93;
  --blue-pale:#e8f1fa;
  --text:#333;
  --muted:#777;
  --white:#fff;
}
*{margin:0;padding:0;box-sizing:border-box}
html,body{width:1200px;height:2832px;overflow:hidden}
body{font-family:"Noto Sans JP",sans-serif;color:var(--text);background:var(--white);position:relative}
.en{font-family:"Montserrat",sans-serif}

/* header */
.site-header{position:absolute;top:0;left:0;width:1200px;height:88px;background:var(--white)}
.logo{position:absolute;left:108px;top:18px;font-family:"Montserrat",sans-serif;font-weight:600;font-size:40px;letter-spacing:2px;color:#222}
.lang{position:absolute;right:100px;top:8px;font-size:11px;color:var(--muted);letter-spacing:1px}
.global-nav{position:absolute;right:96px;top:30px;display:flex}
.global-nav a{display:block;text-align:center;padding:0 16px;border-left:1px solid #ccc;text-decoration:none;color:#222}
.global-nav a:first-child{border-left:none}
.global-nav .nav-en{display:block;font-family:"Montserrat",sans-serif;font-weight:600;font-size:17px;letter-spacing:1px}
.global-nav .nav-ja{display:block;font-size:10px;color:var(--muted);margin-top:3px}

/* hero */
.hero{position:absolute;top:88px;left:0;width:1200px;height:572px;
  background:linear-gradient(180deg,#4f9be0 0%,#9ccaf0 28%,#c9dbe6 42%,#6d8da3 55%,#3f6f7f 70%,#1f6ea8 85%,#2a85c4 100%)}
.hero-copy{position:absolute;left:660px;top:300px;color:var(--white)}
.hero-title{font-family:"Montserrat",sans-serif;font-weight:600;font-size:54px;line-height:1.2;letter-spacing:10px}
.hero-sub{margin-top:12px;font-size:15px;letter-spacing:2px}

/* intro */
.intro{position:absolute;top:672px;left:0;width:1200px;text-align:center}
.intro-title{font-size:29px;font-weight:700;color:var(--blue);letter-spacing:2px}
.intro-text{margin-top:20px;font-size:14px;line-height:2.2;color:var(--text)}

/* feature cards */
.feature-band{position:absolute;top:960px;left:0;width:1200px;height:240px;background:var(--blue)}
.feature-card{position:absolute;top:1012px;width:480px;height:308px;color:var(--white);text-align:center;overflow:hidden}
.feature-card.company{left:108px}
.feature-card.safety{left:608px}
.card-photo{position:absolute;inset:0;background:linear-gradient(180deg,#7fb6e6 0%,#a8c8df 35%,#5b7f9c 65%,#2c4f6e 100%)}
.card-shade{position:absolute;inset:0;background:rgba(10,40,80,.35)}
.badge{position:absolute;left:50%;top:60px;transform:translateX(-50%);width:150px;height:150px;border-radius:50%;border:2px solid var(--white);background:rgba(30,100,180,.45);display:flex;flex-direction:column;align-items:center;justify-content:center}
.badge-en{font-family:"Montserrat",sans-serif;font-weight:600;font-size:24px;letter-spacing:2px}
.badge-ja{font-size:12px;margin-top:4px}
.card-text{position:absolute;left:0;right:0;top:226px;font-size:12px}
.more-btn{position:absolute;left:50%;transform:translateX(-50%);bottom:14px;width:120px;height:26px;border:1px solid var(--white);font-family:"Montserrat",sans-serif;font-size:11px;letter-spacing:2px;line-height:24px}

/* bus */
.bus{position:absolute;top:1480px;left:0;width:1200px;height:300px;color:var(--white);text-align:center}
.bus-photo{position:absolute;inset:0;background:linear-gradient(180deg,#6e8fb0 0%,#8eaac4 40%,#c8d3dc 62%,#6f7a84 80%,#4b5560 100%)}
.bus-shade{position:absolute;inset:0;background:rgba(15,60,120,.35)}
.bus .badge{top:22px;width:180px;height:180px}
.bus .more-btn{bottom:26px}

/* information */
.information{position:absolute;top:1900px;left:108px;width:980px}
.info-head{position:absolute;left:0;top:0}
.info-title{font-family:"Montserrat",sans-serif;font-weight:700;font-size:26px;color:var(--blue);letter-spacing:2px;padding-bottom:6px;border-bottom:2px solid var(--blue)}
.info-sub{font-size:12px;color:var(--muted);margin-top:8px}
.news-list{position:absolute;left:324px;top:38px;width:656px;list-style:none}
.news-item{display:flex;padding:12px 16px;font-size:11px;line-height:1.8}
.news-item.alt{background:var(--blue-pale)}
.news-date{width:104px;flex-shrink:0;font-family:"Montserrat",sans-serif;color:var(--text)}
.news-body{color:var(--text)}

/* contact */
.contact-band{position:absolute;top:2412px;left:0;width:1200px;height:420px;background:var(--blue)}
.contact{position:absolute;top:2320px;left:188px;width:824px;height:240px;color:var(--white)}
.contact-photo{position:absolute;inset:0;background:linear-gradient(90deg,#7c8ea2 0%,#a6b6c5 40%,#8ea0b2 70%,#64788e 100%)}
.contact-shade{position:absolute;inset:0;background:rgba(20,70,140,.45)}
.contact-title{position:absolute;top:30px;left:0;right:0;text-align:center;font-family:"Montserrat",sans-serif;font-weight:600;font-size:22px;letter-spacing:3px}
.contact-tel{position:absolute;left:72px;top:92px;font-family:"Montserrat",sans-serif;font-weight:600;font-size:27px;letter-spacing:2px;line-height:48px}
.contact-tel div,.contact-mail{display:flex;align-items:center;gap:10px}
.contact-mail{position:absolute;left:440px;top:130px;font-size:20px;letter-spacing:2px}

/* footer */
.site-footer{position:absolute;top:2560px;left:0;width:1200px;height:272px;color:var(--white)}
.footer-name{position:absolute;left:108px;top:100px;font-size:15px;letter-spacing:1px}
.footer-addr{position:absolute;left:108px;top:128px;font-size:10px;line-height:1.8}
.footer-nav{position:absolute;left:864px;top:100px;list-style:none;font-size:11px;line-height:1.7}
.footer-nav li::before{content:"- ";}
</style>
</head>
<body>

<header class="site-header">
  <div class="logo">LOGO</div>
  <div class="lang">日本 | English | 中文 | Tel</div>
  <nav class="global-nav">
    <a href="#"><span class="nav-en">HOME</span><span class="nav-ja">ホーム</span></a>
    <a href="#"><span class="nav-en">COMPANY</span><span class="nav-ja">会社概要</span></a>
    <a href="#"><span class="nav-en">BUS</span><span class="nav-ja">バスのご案内</span></a>
    <a href="#"><span class="nav-en">SAFETY</span><span class="nav-ja">安全への取り組み</span></a>
    <a href="#"><span class="nav-en">CONTACT</span><span class="nav-ja">お問い合わせ</span></a>
  </nav>
</header>

<section class="hero" role="img" aria-label="海辺の高層ビル街と港を見下ろす都市の風景">
  <div class="hero-copy">
    <h1 class="hero-title">SAFETY<br>HIGH QUALITY</h1>
    <p class="hero-sub">○○○○○○○○○ <span class="en">Company Limited</span></p>
  </div>
</section>

<section class="intro">
  <h2 class="intro-title">より一層安全・安心なお客様サービスの実現へ</h2>
  <p class="intro-text">○○○○は、"Safety"と"High Quality"をモットーとし、<br>これからも「確かな安全・安心」と「素敵な旅のひととき」で快適な旅をお手伝いします。</p>
</section>

<div class="feature-band"></div>

<a class="feature-card company" href="#">
  <div class="card-photo" role="img" aria-label="青空の下の高層ビル群"></div>
  <div class="card-shade"></div>
  <div class="badge"><span class="badge-en">COMPANY</span><span class="badge-ja">会社概要</span></div>
  <p class="card-text">私たちの会社について、理念や沿革をご紹介します。</p>
  <div class="more-btn">MORE</div>
</a>

<a class="feature-card safety" href="#">
  <div class="card-photo" role="img" aria-label="港に面した高層ビルの街並み"></div>
  <div class="card-shade"></div>
  <div class="badge"><span class="badge-en">SAFETY</span><span class="badge-ja">安全対策について</span></div>
  <p class="card-text">日々の点検や教育など、安全への取り組みをご紹介します。</p>
  <div class="more-btn">MORE</div>
</a>

<section class="bus">
  <div class="bus-photo" role="img" aria-label="駐車場に並ぶ白い観光バス"></div>
  <div class="bus-shade"></div>
  <div class="badge"><span class="badge-en">BUS</span><span class="badge-ja">車両のご案内</span></div>
  <div class="more-btn">詳しく見る</div>
</section>

<section class="information">
  <div class="info-head">
    <h2 class="info-title">INFORMATION</h2>
    <p class="info-sub">○○○○○からのお知らせ</p>
  </div>
  <ul class="news-list">
    <li class="news-item"><span class="news-date">2020/10/01</span><span class="news-body">一般貸切（観光）のご案内<br>新しい車両の導入に伴い、貸切プランの内容を一部変更いたしました。<br>詳しくは各車両のご案内ページをご覧ください。</span></li>
    <li class="news-item alt"><span class="news-date">2020/09/15</span><span class="news-body">ホームページをリニューアルしました。</span></li>
    <li class="news-item"><span class="news-date">2020/08/20</span><span class="news-body">一般貸切（観光）のご案内<br>秋の行楽シーズンに向けたご予約の受付を開始いたしました。<br>お早めにお問い合わせください。</span></li>
    <li class="news-item alt"><span class="news-date">2020/07/01</span><span class="news-body">ホームページをリニューアルしました。</span></li>
  </ul>
</section>

<div class="contact-band"></div>

<section class="contact">
  <div class="contact-photo" role="img" aria-label="ビルの前に停まるバス"></div>
  <div class="contact-shade"></div>
  <h2 class="contact-title">CONTACT</h2>
  <div class="contact-tel">
    <div><svg width="24" height="24" viewBox="0 0 24 24"><path fill="#fff" d="M6.6 10.8a15 15 0 006.6 6.6l2.2-2.2a1 1 0 011-.25 11.4 11.4 0 003.6.57 1 1 0 011 1V20a1 1 0 01-1 1A17 17 0 013 4a1 1 0 011-1h3.5a1 1 0 011 1 11.4 11.4 0 00.57 3.6 1 1 0 01-.25 1z"/></svg>0123-456-789</div>
    <div><svg width="24" height="24" viewBox="0 0 24 24"><path fill="#fff" d="M6.6 10.8a15 15 0 006.6 6.6l2.2-2.2a1 1 0 011-.25 11.4 11.4 0 003.6.57 1 1 0 011 1V20a1 1 0 01-1 1A17 17 0 013 4a1 1 0 011-1h3.5a1 1 0 011 1 11.4 11.4 0 00.57 3.6 1 1 0 01-.25 1z"/></svg>0123-456-789</div>
  </div>
  <div class="contact-mail"><svg width="26" height="20" viewBox="0 0 26 20"><rect x="1" y="1" width="24" height="18" fill="none" stroke="#fff" stroke-width="2"/><path d="M1 1l12 10L25 1" fill="none" stroke="#fff" stroke-width="2"/></svg>メールフォーム</div>
</section>

<footer class="site-footer">
  <p class="footer-name">○○○○○○○○株式会社</p>
  <p class="footer-addr">〒000-0000　○○県○○市○○町1-2-3<br>TEL 0123-456-789<br>FAX 0123-456-780</p>
  <ul class="footer-nav">
    <li>ホーム</li>
    <li>会社概要</li>
    <li>バスのご案内</li>
    <li>安全への取り組み</li>
    <li>お問い合わせ</li>
  </ul>
</footer>

</body>
</html>
```